Brela Coffee Cups

We already have Brela Coffee cups, but the existing design is dated.
It needs a fresh modern look. (this look will be used with all Brela advertising..
But the look and font of the word Brela needs to say the same.

Industry/Entity Type

Advertising

```html
<!DOCTYPE html>
<html lang="en">
<head>
<meta charset="utf-8">
<title>Brela Coffee – Cup Wrap</title>
<link href="https://fonts.googleapis.com/css2?family=Rosario:wght@700&family=Open+Sans:wght@400&display=swap" rel="stylesheet">
<style>
  :root {
    --page: #f4f4f4;
    --cup-yellow: #fdc314;
    --band-light: #f2b40e;
    --band-deep: #e3a00a;
    --white: #ffffff;
    --trim: rgba(255, 255, 255, 0.55);
  }
  html, body {
    margin: 0;
    padding: 0;
    overflow: hidden;
  }
  .canvas {
    width: 810px;
    height: 1200px;
    background: var(--page);
    position: relative;
    overflow: hidden;
  }
  .cup-wrap {
    position: absolute;
    left: 0;
    top: 384px;
    width: 810px;
    height: 432px;
    filter: drop-shadow(0 6px 8px rgba(0, 0, 0, 0.12));
  }
  .wrap-body { fill: var(--cup-yellow); }
  .lettering-band { fill: url(#band-tone); }
  .trim-line {
    fill: none;
    stroke: var(--trim);
    stroke-width: 1;
    stroke-dasharray: 2 3;
  }
  .brand-name {
    font-family: "Rosario", sans-serif;
    font-weight: 700;
    font-size: 58px;
    fill: var(--white);
  }
  .brand-rule { stroke: var(--white); stroke-width: 1; }
  .web-address {
    font-family: "Open Sans", sans-serif;
    font-size: 11px;
    fill: var(--white);
    letter-spacing: 0.5px;
  }
  .order-option {
    font-family: "Open Sans", sans-serif;
    font-size: 9.5px;
    fill: var(--white);
    letter-spacing: 0.6px;
  }
  .tick-dot { fill: var(--white); }
</style>
</head>
<body>
<main class="canvas">
  <svg class="cup-wrap" viewBox="0 140 900 480" aria-label="Brela Coffee cup wrap, flat die-line">
    <defs>
      <linearGradient id="band-tone" x1="0" y1="0" x2="1" y2="0">
        <stop offset="0" stop-color="var(--band-light)"/>
        <stop offset="0.5" stop-color="var(--band-deep)"/>
        <stop offset="1" stop-color="var(--band-light)"/>
      </linearGradient>
    </defs>

    <path class="wrap-body" d="M30,215 Q447,95 865,215 L755,608 Q450,522 150,608 Z"/>

    <path class="lettering-band" role="img" aria-label="Large decorative lettering band along the top rim"
          d="M30,215 Q447,95 865,215 L845,285 Q447,170 50,285 Z"/>
    <path class="lettering-band" role="img" aria-label="Large decorative lettering band along the bottom rim"
          d="M137,555 Q450,460 772,555 L755,608 Q450,522 150,608 Z"/>

    <path class="trim-line" d="M62,228 Q447,118 832,228 L738,585 Q450,504 168,585 Z"/>

    <g class="brand-panel" transform="rotate(-4 268 360)">
      <text class="brand-name" x="268" y="374" text-anchor="middle">Brela</text>
      <line class="brand-rule" x1="173" y1="386" x2="363" y2="386"/>
      <text class="web-address" x="277" y="438" text-anchor="middle">brelacoffee.com.au</text>
    </g>

    <g class="brand-panel" transform="rotate(4 624 360)">
      <text class="brand-name" x="624" y="374" text-anchor="middle">Brela</text>
      <line class="brand-rule" x1="529" y1="386" x2="719" y2="386"/>
      <text class="web-address" x="612" y="438" text-anchor="middle">brelacoffee.com.au</text>
    </g>

    <g class="tick-dots">
      <circle class="tick-dot" cx="92" cy="295" r="5"/>
      <circle class="tick-dot" cx="98" cy="315" r="5"/>
      <circle class="tick-dot" cx="104" cy="335" r="5"/>
      <circle class="tick-dot" cx="110" cy="356" r="5"/>
      <circle class="tick-dot" cx="116" cy="376" r="5"/>
      <circle class="tick-dot" cx="121" cy="396" r="5"/>
      <circle class="tick-dot" cx="127" cy="416" r="5"/>
      <circle class="tick-dot" cx="132" cy="436" r="5"/>
      <circle class="tick-dot" cx="138" cy="456" r="5"/>
    </g>

    <g class="order-options" text-anchor="end">
      <text class="order-option" x="808" y="300" transform="rotate(12 808 300)">cap</text>
      <text class="order-option" x="802" y="320" transform="rotate(12 802 320)">latte</text>
      <text class="order-option" x="797" y="340" transform="rotate(12 797 340)">flat white</text>
      <text class="order-option" x="791" y="360" transform="rotate(12 791 360)">long black</text>
      <text class="order-option" x="785" y="380" transform="rotate(12 785 380)">mocha</text>
      <text class="order-option" x="779" y="401" transform="rotate(12 779 401)">choc</text>
      <text class="order-option" x="773" y="421" transform="rotate(12 773 421)">decaf</text>
      <text class="order-option" x="767" y="442" transform="rotate(12 767 442)">soy</text>
      <text class="order-option" x="761" y="462" transform="rotate(12 761 462)">sugar</text>
    </g>
  </svg>
</main>
</body>
</html>
```